Rabbit Meat Label

We need a label for a shrink-wrapped tray of rabbit. The label does not need to be fancy, we just want a simple sticker to show customers a mock-up of what it may look like. The label is approximately 5" x 2.75". The label will go on top of the rabbit, so it will not lay flat. Please take that into consideration

The rabbit specifically is farm raised. Whole cut-up with 2 fore-legs, 2 hind legs and back.

There is nutritional information on the back, so please mention that somewhere on the label.

Industry/Entity Type

Farm

Requirements
Must have
• Please leave spaces for FQRB seals and other misc items. They are about 0.5" squares.
Should not have
• Do not have anything like "Made in the USA" or "All Natural." This will be added later, if need be.

```html
<!DOCTYPE html>
<html lang="en">
<head>
<meta charset="utf-8">
<title>Rabbit Meat Label</title>
<link rel="stylesheet" href="https://fonts.googleapis.com/css2?family=PT+Sans:wght@400;700&family=Carlito&display=swap">
<style>
  :root {
    --paper: #ffffff;
    --navy: #0c1577;
    --red: #c00000;
    --deep-red: #a50f0f;
    --box-red: #a32020;
    --seal-grey: #8a8a8a;
    --ink: #000000;
    --art-tone: #e4e4e4;
  }
  html, body {
    margin: 0;
    padding: 0;
    overflow: hidden;
    background: var(--paper);
  }
  .label {
    position: relative;
    width: 1200px;
    height: 661px;
    background: var(--paper);
    overflow: hidden;
  }
  .frame-outer {
    position: absolute;
    left: 43px; top: 43px;
    width: 1114px; height: 576px;
    box-sizing: border-box;
    border: 2px solid var(--navy);
  }
  .frame-inner {
    position: absolute;
    left: 53px; top: 53px;
    width: 1094px; height: 558px;
    box-sizing: border-box;
    border: 10px solid var(--navy);
  }
  .rabbit-art {
    position: absolute;
    left: 162px; top: 116px;
    width: 232px; height: 452px;
    background: radial-gradient(ellipse at 50% 60%, #d6d6d6, var(--art-tone) 70%, #f3f3f3);
    border-radius: 40% 40% 45% 45% / 30% 30% 40% 40%;
  }
  .title {
    position: absolute;
    left: 420px; top: 102px;
    width: 330px;
    margin: 0;
    text-align: center;
    font-family: "PT Sans", sans-serif;
    font-weight: 700;
    font-size: 84px;
    line-height: 1;
    letter-spacing: 1px;
    color: var(--red);
    -webkit-text-stroke: 1px #7a0000;
  }
  .subtitle {
    position: absolute;
    left: 420px; top: 228px;
    width: 330px;
    margin: 0;
    text-align: center;
    font-family: "PT Sans", sans-serif;
    font-weight: 700;
    font-size: 27px;
    line-height: 1;
    color: var(--deep-red);
  }
  .seal-space {
    position: absolute;
    left: 523px; top: 301px;
    width: 120px; height: 120px;
    box-sizing: border-box;
    border: 1.5px solid var(--seal-grey);
  }
  .cut-box {
    position: absolute;
    left: 789px; top: 214px;
    width: 316px; height: 312px;
    box-sizing: border-box;
    border: 2px solid var(--box-red);
    padding: 20px 0 0 12px;
    font-family: "Carlito", sans-serif;
    font-size: 39px;
    line-height: 56px;
    color: var(--ink);
  }
  .cut-box p { margin: 0; }
  .cut-list {
    list-style: none;
    margin: 0;
    padding: 0;
  }
  .cut-list li::before {
    content: "";
    display: inline-block;
    width: 9px; height: 9px;
    border-radius: 50%;
    background: var(--ink);
    margin: 0 8px 0 2px;
    vertical-align: middle;
  }
  .back-note {
    position: absolute;
    left: 520px; top: 543px;
    width: 500px;
    margin: 0;
    text-align: center;
    font-family: "Carlito", sans-serif;
    font-size: 24px;
    line-height: 1;
    color: var(--ink);
  }
</style>
</head>
<body>
  <main class="label">
    <div class="frame-outer"></div>
    <div class="frame-inner"></div>
    <div class="rabbit-art" role="img" aria-label="Line drawing of a rabbit sitting upright, facing right"></div>
    <h1 class="title">RABBIT</h1>
    <p class="subtitle">FARM RAISED</p>
    <div class="seal-space" aria-label="Space for inspection seal"></div>
    <section class="cut-box">
      <p>Whole cut-up<br>with:</p>
      <ul class="cut-list">
        <li>2 fore-legs</li>
        <li>2 hind legs</li>
        <li>back.</li>
      </ul>
    </section>
    <p class="back-note">nutritional information on the back</p>
  </main>
</body>
</html>
```